Luminously Grounded Vitality

We want to design a business card that is modern and appealing for an innovative psychedelic telemedicine company that provides at-home ketamine-assisted therapy along with wellness, longevity, and anti-aging medicines. We want to use our deep purple and white plus other colors you can find on our website. We don't have any strict brand guidelines yet so feel free to get creative. We want a very professional, but technology first modern design that will instill trust, peace, calm, but also be attractive to investors in the healthcare and SaaS space.

```html
<!DOCTYPE html>
<html lang="en">
<head>
<meta charset="utf-8">
<title>Luminously Grounded Vitality – Business Card</title>
<link href="https://fonts.googleapis.com/css2?family=Open+Sans:wght@400;600;700&display=swap" rel="stylesheet">
<style>
  :root {
    --stage: #2b2a30;
    --deep-purple: #2a1740;
    --pattern-purple: #4a2a6e;
    --mark-violet: #8c6fbf;
    --brand-pink: #c07ab0;
    --lavender: #b7a4d6;
    --white: #ffffff;
  }
  * { margin: 0; padding: 0; box-sizing: border-box; }
  html, body {
    width: 1200px; height: 780px; overflow: hidden;
    background: var(--stage);
    font-family: "Open Sans", sans-serif;
  }
  .canvas {
    position: relative; width: 1200px; height: 780px;
  }
  .card {
    position: absolute; top: 235px;
    width: 540px; height: 310px;
    border-radius: 22px; overflow: hidden;
    background: var(--deep-purple);
    border: 3px solid var(--brand-pink);
  }
  .card-front { left: 40px; }
  .card-back { left: 620px; }

  /* Front side */
  .pattern-field {
    position: absolute; inset: 0;
    background: linear-gradient(135deg, var(--deep-purple) 0%, var(--pattern-purple) 50%, var(--deep-purple) 100%);
  }
  .front-brand {
    position: absolute; inset: 0;
    display: flex; align-items: center; justify-content: center; gap: 12px;
  }
  .brand-dot {
    width: 30px; height: 30px; border-radius: 50%;
    background: var(--mark-violet); flex: none;
  }
  .front-brand .brand-name {
    font-size: 24px; font-weight: 400; color: var(--lavender);
  }

  /* Info side */
  .back-brand {
    position: absolute; left: 26px; top: 36px;
    display: flex; align-items: center; gap: 12px;
  }
  .back-brand .brand-name {
    font-size: 21px; font-weight: 400; color: var(--brand-pink);
  }
  .accent-bar {
    position: absolute; left: 26px; top: 138px;
    width: 6px; height: 46px; background: var(--brand-pink);
  }
  .person-name {
    position: absolute; left: 42px; top: 132px;
    font-size: 21px; font-weight: 700; color: var(--brand-pink);
  }
  .person-role {
    position: absolute; left: 42px; top: 163px;
    font-size: 12.5px; color: var(--white);
  }
  .divider {
    position: absolute; left: 292px; top: 148px;
    width: 222px; height: 2px; background: var(--white);
  }
  .address {
    position: absolute; right: 26px; top: 160px;
    font-size: 11px; line-height: 1.45; color: var(--white); text-align: right;
  }
  .contacts {
    position: absolute; left: 42px; top: 204px;
    list-style: none;
  }
  .contacts li {
    display: flex; align-items: center; gap: 8px;
    font-size: 12.5px; line-height: 20px; color: var(--white);
  }
  .contacts svg { width: 12px; height: 12px; flex: none; }
  .edge-bands { position: absolute; inset: 0; }
</style>
</head>
<body>
<main class="canvas">

  <section class="card card-front" aria-label="Card front">
    <div class="pattern-field" role="img" aria-label="Repeating brand symbol pattern in soft purple tones"></div>
    <div class="front-brand">
      <span class="brand-dot"></span>
      <span class="brand-name">Luminously Grounded Vitality</span>
    </div>
  </section>

  <section class="card card-back" aria-label="Card back with contact details">
    <div class="back-brand">
      <span class="brand-dot"></span>
      <span class="brand-name">Luminously Grounded Vitality</span>
    </div>

    <span class="accent-bar"></span>
    <h1 class="person-name">Maren Okafor, FNP-C</h1>
    <p class="person-role">Co-founder, Chief Clinical Officer</p>
    <span class="divider"></span>

    <p class="address">240 Alder Lane, Suite 900,<br>Fairview, CO, United States,<br>Colorado</p>

    <ul class="contacts">
      <li>
        <svg viewBox="0 0 12 12" aria-hidden="true"><path d="M2.5 1 L4.5 1 L5.2 3.6 L4 4.6 Q5 7 7.4 8 L8.4 6.8 L11 7.5 L11 9.5 Q11 11 9.5 11 Q1 10 1 2.5 Q1 1 2.5 1 Z" fill="var(--brand-pink)"/></svg>
        +1 800-555-0147
      </li>
      <li>
        <svg viewBox="0 0 12 12" aria-hidden="true"><circle cx="6" cy="6" r="5" fill="none" stroke="var(--brand-pink)" stroke-width="1.3"/><ellipse cx="6" cy="6" rx="2.2" ry="5" fill="none" stroke="var(--brand-pink)" stroke-width="1"/><line x1="1" y1="6" x2="11" y2="6" stroke="var(--brand-pink)" stroke-width="1"/></svg>
        www.luminouslygrounded.com
      </li>
      <li>
        <svg viewBox="0 0 12 12" aria-hidden="true"><rect x="1" y="2.5" width="10" height="7" rx="1" fill="var(--brand-pink)"/><path d="M1.5 3 L6 6.5 L10.5 3" fill="none" stroke="var(--deep-purple)" stroke-width="1"/></svg>
        hello@luminouslygrounded.com
      </li>
    </ul>

    <svg class="edge-bands" viewBox="0 0 540 310" preserveAspectRatio="none" aria-hidden="true">
      <polygon points="372,236 540,236 540,310 420,310 452,262 360,262" fill="var(--brand-pink)"/>
      <polygon points="140,310 140,294 330,294 366,266 440,266 410,310" fill="var(--lavender)"/>
      <polyline points="140,292 328,292 364,264 446,264" fill="none" stroke="var(--brand-pink)" stroke-width="3"/>
    </svg>
  </section>

</main>
</body>
</html>
```